Website Redesign - Spa Barn Depot

We need a new website for a hot tub dealer. This is a redesign of the existing site. The goal of the site is to drive phone calls and emails to book warehouse viewings, not to sell inventory from the website. The dealer sells both new and used hot tubs. I'd like to see some of the big name brands reflected; he's a small dealer and needs trust factor. He also has a great rating with QTR. We are no longer going to use the site to list inventory. This is a lead generation site. The existing site is boring. We would like to see some imagination. The client has a rustic back woods warehouse. He's a very knowledgeable yet quirky client. He doesn't want people showing up thinking that this is a big box fancy dealership. He's like the Bulkmart warehouse of hot tub dealers and the site should reflect that. No frills, honest advice, etc. www.spabarndepot.example

Target Market(s)

Surrey, Langley, Vancouver and area homeowners looking for new and used hot tubs

Number of Pages Required

5+ page

Font styles to use
Serif
Sans Serif

Colors

Designer to choose colors to be used in the design.

Requirements
Must have
• Home page

```html
<!DOCTYPE html>
<html lang="en">
<head>
<meta charset="utf-8">
<title>Spa Barn Depot</title>
<link rel="stylesheet" href="https://fonts.googleapis.com/css2?family=Lato:ital,wght@0,400;0,700;0,900;1,400&display=swap">
<style>
:root{
  --blue:#2b55a6;
  --blue-dark:#1e2f86;
  --sky:#5aaee8;
  --ink:#3a3a3a;
  --text:#444;
  --muted:#f2f2f2;
  --white:#fff;
}
*{box-sizing:border-box;margin:0;padding:0}
html,body{width:1200px;height:2308px;overflow:hidden}
body{font-family:'Lato',Arial,sans-serif;color:var(--text);background:var(--white);position:relative}
section,header,nav,footer,.topbar{position:relative;width:1200px}
.abs{position:absolute}

.topbar{height:57px;background:var(--muted);text-align:center;font-style:italic;font-size:15px;color:var(--blue);line-height:57px}
.topbar span{margin:0 10px}

.site-header{height:94px}
.brand{left:77px;top:24px;display:flex;align-items:center;gap:10px}
.brand-dot{width:18px;height:18px;border-radius:50%;background:var(--sky)}
.brand-name{font-size:38px;font-weight:900;color:var(--blue);letter-spacing:-0.5px}
.contact-item{top:20px;display:flex;gap:12px;align-items:flex-start}
.contact-item svg{width:38px;height:38px;margin-top:6px}
.contact-label{font-size:19px;font-weight:700;color:var(--ink);line-height:22px}
.contact-value{font-size:20px;color:var(--blue);line-height:26px}
.contact-call{left:623px}
.contact-email{left:858px}

.main-nav{height:49px;background:linear-gradient(#4aa9e6,#2f5fb4 55%,#23358e)}
.main-nav a{position:absolute;top:0;line-height:49px;color:var(--white);font-size:14px;text-decoration:none;letter-spacing:.2px;white-space:nowrap}
.cart{right:74px;display:flex;align-items:center;gap:6px;font-size:16px!important}

.hero{height:511px;overflow:hidden;background:linear-gradient(160deg,#e7eef2 0%,#6fc1e0 35%,#3aa2d2 55%,#bfe1ec 80%,#f1f3f4 100%)}
.hero-title{width:100%;top:160px;text-align:center;color:var(--white);font-weight:900;text-shadow:0 2px 6px rgba(0,0,0,.25)}
.hero-title .l1{font-size:44px;line-height:50px;display:block}
.hero-title .l2{font-size:52px;line-height:56px;display:block}
.btn{display:inline-block;text-align:center;color:var(--white);font-weight:700;font-size:15px;text-decoration:none;background:linear-gradient(#3c6ec4,#22389a)}
.hero-btn{left:531px;top:274px;width:151px;height:43px;line-height:43px}
.dots{left:565px;top:457px;display:flex;gap:8px}
.dots i{width:11px;height:11px;border-radius:50%;background:var(--white)}
.dots i:first-child{background:var(--sky)}
.hero-wave{left:0;bottom:0;width:1200px;height:80px}

.about{height:389px}
.section-title{font-size:28px;font-weight:700;color:var(--ink);letter-spacing:.3px}
.about .section-title{left:74px;top:52px}
.about-text{left:74px;top:100px;width:600px;font-size:14px;line-height:26px;color:var(--text)}
.about-btn{left:74px;top:281px;width:152px;height:43px;line-height:43px}
.video{left:705px;top:54px;width:421px;height:270px;border:5px solid #b5b5b5;background:linear-gradient(90deg,#8a7c72 0%,#b7aca4 45%,#e7e2d8 70%,#f4f0e8 100%);overflow:hidden}
.video-play{left:180px;top:105px;width:52px;height:52px}
.video-name{right:6px;bottom:26px;color:var(--white);font-size:26px;font-weight:400;text-align:right}
.video-role{right:6px;bottom:8px;color:var(--white);font-size:14px;text-align:right}

.guides{height:461px}
.guides-bg{left:0;top:-10px;width:1200px;height:480px}
.guide-card{top:92px;width:511px;height:280px;text-align:center;color:var(--white);background:linear-gradient(135deg,#5a55b8,#3f47ac 50%,#5c64c4)}
.guide-card h3{margin-top:49px;font-size:26px;font-weight:700}
.guide-card .lead{margin-top:18px;font-size:16px;color:#6fb6f2}
.guide-card .sub{margin-top:4px;font-size:14px}
.guide-card .btn{margin-top:32px;width:151px;height:42px;line-height:42px}
.card-used{left:75px}
.card-new{left:615px}

.brands{height:311px;text-align:center}
.brands .section-title{position:absolute;width:100%;top:42px;font-size:26px}
.brands-sub{position:absolute;width:100%;top:94px;font-size:15px;color:var(--ink)}
.brand-col{top:148px;width:520px;text-align:center}
.brand-col h4{font-size:17px;font-weight:700;color:var(--blue-dark);margin-bottom:6px}
.brand-col p{font-size:13px;line-height:27px;color:var(--ink);white-space:nowrap}
.col-dealer{left:71px}
.col-used{left:602px}

.cta{height:239px;background:linear-gradient(180deg,#223e88,#1a2a6e 60%,#11185a);text-align:center;color:var(--white)}
.cta h2{padding-top:52px;font-size:28px;font-weight:700;letter-spacing:.3px}
.cta p{margin-top:17px;font-size:15px}
.cta-btn{margin-top:22px;display:inline-block;width:150px;height:43px;line-height:43px;background:var(--white);color:var(--blue-dark);font-weight:700;font-size:15px;text-decoration:none}

.site-footer{height:197px}
.footer-nav{left:74px;top:42px;display:flex;gap:27px}
.footer-nav a{font-size:13px;color:var(--ink);text-decoration:none}
.copyright{left:74px;top:79px;font-size:12px;color:var(--ink)}
.social{left:74px;top:124px;display:flex;gap:18px}
.social span{font-size:13px;font-weight:700;color:var(--blue)}
.rating{left:857px;top:42px;display:flex;gap:8px;align-items:center}
.rating-badge{width:127px;height:50px;border-radius:5px;background:#0f5e84}
.rating-text{font-size:12px;font-weight:700;color:var(--blue-dark);line-height:20px}
</style>
</head>
<body>

<div class="topbar"><span>Free local delivery to most Lower Mainland addresses</span>|<span>One year extended warranty on all new tubs</span></div>

<header class="site-header">
  <div class="brand abs"><span class="brand-dot"></span><span class="brand-name">Spa Barn Depot</span></div>
  <div class="contact-item contact-call abs">
    <svg viewBox="0 0 38 38"><circle cx="19" cy="19" r="17.5" fill="none" stroke="#2b55a6" stroke-width="2"/><path d="M13 11c1-1 2-1 3 0l2 3c.5 1 .3 1.7-.5 2.3l-1 .8c1 2 3 4 5 5l.8-1c.6-.8 1.3-1 2.3-.5l3 2c1 1 1 2 0 3l-1.5 1.5c-4 1-13-8-12-12z" fill="#2b55a6"/></svg>
    <div><div class="contact-label">CALL:</div><div class="contact-value">604-555-0142</div></div>
  </div>
  <div class="contact-item contact-email abs">
    <svg viewBox="0 0 38 38"><circle cx="19" cy="19" r="18" fill="#2b55a6"/><rect x="11" y="13" width="16" height="12" rx="1.5" fill="#fff"/><path d="M11.5 14l7.5 6 7.5-6" fill="none" stroke="#2b55a6" stroke-width="1.6"/></svg>
    <div><div class="contact-label">EMAIL:</div><div class="contact-value">spabarndepot@mail.example</div></div>
  </div>
</header>

<nav class="main-nav">
  <a style="left:74px">HOME</a>
  <a style="left:160px">NEW HOT TUBS</a>
  <a style="left:309px">USED HOT TUBS</a>
  <a style="left:462px">TUB REMOVAL</a>
  <a style="left:603px">TESTIMONIALS</a>
  <a style="left:748px">ARTICLES</a>
  <a style="left:855px">CONTACT</a>
  <a class="cart"><svg width="18" height="16" viewBox="0 0 18 16"><path d="M0 1h3l2.5 9h9.5l2-7H4.5" fill="none" stroke="#fff" stroke-width="2"/><circle cx="7" cy="13.5" r="1.6" fill="#fff"/><circle cx="14" cy="13.5" r="1.6" fill="#fff"/></svg>(0)</a>
</nav>

<section class="hero" role="img" aria-label="Photo of a couple relaxing in a bubbling outdoor hot tub">
  <h1 class="hero-title abs"><span class="l1">WELCOME TO</span><span class="l2">SPA BARN DEPOT</span></h1>
  <a class="btn hero-btn abs">VIEW ALL TUBS</a>
  <div class="dots abs"><i></i><i></i><i></i><i></i></div>
  <svg class="hero-wave abs" viewBox="0 0 1200 80" preserveAspectRatio="none"><path d="M0 10 C300 70 700 80 1200 20 L1200 80 L0 80Z" fill="#fff"/></svg>
</section>

<section class="about">
  <h2 class="section-title abs">ABOUT SPA BARN DEPOT</h2>
  <p class="about-text abs">Spa Barn Depot is a rustic warehouse concept in a casual setting in the Port Kells area of Surrey.&nbsp; Simple, efficient and practical.&nbsp; Low bling, no schmooze.&nbsp; We are dealers for many brand names, and sell both new and used hot tubs so we have a huge selection to choose from. We like to think of ourselves as catering to the more sensible, intelligent shopper. We tend to attract the kind of people who don't want a slick a slick sales pitch and don't need a fancy showroom...</p>
  <a class="btn about-btn abs">READ MORE</a>
  <div class="video abs" role="img" aria-label="Video still of the owner speaking in the warehouse">
    <svg class="video-play abs" viewBox="0 0 52 52"><circle cx="26" cy="26" r="26" fill="#fff"/><path d="M20 15l17 11-17 11z" fill="#555"/></svg>
    <div class="video-name abs">DALE CORRIGAN</div>
    <div class="video-role abs">OWNER, SPA BARN DEPOT</div>
  </div>
</section>

<section class="guides">
  <svg class="guides-bg abs" viewBox="0 0 1200 480" preserveAspectRatio="none">
    <defs><linearGradient id="paleBand" x1="0" y1="0" x2="0" y2="1"><stop offset="0" stop-color="#f4f8fd"/><stop offset=".5" stop-color="#e3edf9"/><stop offset="1" stop-color="#cddff3"/></linearGradient></defs>
    <path d="M0 45 C350 5 800 60 1200 0 L1200 430 C900 460 500 440 300 470 C180 480 80 470 0 455Z" fill="url(#paleBand)"/>
  </svg>
  <div class="guide-card card-used abs" role="img" aria-label="Close-up of hot tub jets under blue water">
    <h3>BUYING USED SPAS</h3>
    <p class="lead">Beware of buying used hot tubs</p>
    <p class="sub">15 things to watch out for before you decide.</p>
    <a class="btn">VIEW ALL</a>
  </div>
  <div class="guide-card card-new abs" role="img" aria-label="Close-up of a new hot tub shell under blue water">
    <h3>BUYING A NEW HOT TUB?</h3>
    <p class="lead">Before you get yourself in hot water, here are</p>
    <p class="sub">29 things to know about buying a new hot tub.</p>
    <a class="btn">VIEW ALL</a>
  </div>
</section>

<section class="brands">
  <h2 class="section-title">HOT TUB BRANDS</h2>
  <p class="brands-sub">Over 250 model options, both new and used, from over two dozen brands!</p>
  <div class="brand-col col-dealer abs">
    <h4>AUTHORIZED DEALERFOR</h4>
    <p>BAY SPAS | DAYBREAK | STILLWATER | CEDAR COVE | NORTH SHORE | PRIME<br>REPOSE | SUMMITLINE | RIVER-TO-PEAK | HAVEN | LEVEL NINE |<br>CAMPWELL &nbsp;| &nbsp;NOVARA &nbsp;| &nbsp;EASYSTREAM.</p>
  </div>
  <div class="brand-col col-used abs">
    <h4>USED HOT TUBS BRANDS</h4>
    <p>BUBBLA® &nbsp;| &nbsp;SUNDRIFT &nbsp;| &nbsp;LOUNGEMAN &nbsp;| &nbsp;REGENCY &nbsp;| &nbsp;GLACIER &nbsp;| &nbsp;TIDEWATER &nbsp;|<br>SHORE SPAS &nbsp;| &nbsp;FOXTAIL SPAS &nbsp;| &nbsp;SERENA &nbsp;| &nbsp;DRIFTWOOD &nbsp;| &nbsp;AQUA9 SPAS &nbsp;|<br>VAXO &nbsp;| &nbsp;HALCYON &nbsp;| &nbsp;ENDLESS &nbsp;| &nbsp;NEWTLY AND MORE!</p>
  </div>
</section>

<section class="cta" role="img" aria-label="Dimly lit hot tub with blue water in the background">
  <h2>SCHEDULE AN APPOINTMENT TODAY!</h2>
  <p>Come by for a viewing of our wide range of new and used Hot Tubs.</p>
  <a class="cta-btn">CONTACT US</a>
</section>

<footer class="site-footer">
  <div class="footer-nav abs">
    <a>HOME</a><a>NEW HOT TUBS</a><a>USED HOT TUBS</a><a>TUB REMOVAL</a><a>TESTIMONIALS</a><a>ARTICLES</a><a>CONTACT</a>
  </div>
  <p class="copyright abs">Copyright © 2018. Company Name. All Right Reserved</p>
  <div class="social abs"><span>Friendly</span><span>Chirper</span><span>Snapgram</span><span>LinkUp</span><span>ViewTube</span></div>
  <div class="rating abs">
    <div class="rating-badge" role="img" aria-label="QTR accreditation badge"></div>
    <div class="rating-text">QTR Rating: A+<br>Click for Review</div>
  </div>
</footer>

</body>
</html>
```